Website for Swedish wellness company "Heartmeadow"

We need a website for our Swedish wellness company. The name is "Heartmeadow" . The company is all about sustainablility for our body, soul and planet. We work with coaching, yoga, massage, healthy food, retreats(sports, excercise, sufing), healing and inspirational talks. We are convinced that personal sustainability and a strong spiritual connection to yourself will lead to planetary sustainability. Our customers are both companies and consumers from all over the world. The final design should be clean/simple and you should get a feeling of community, happiness, warmth, connection,, joy, spirituality but still a professional touch.Just got a logo from Pixel Forum and are very happy with it;-)
Updates

Sorry I was too enthusiastic posting this project. Of course I will give you some text as well för the different pages! I will see to that it is finished by friday so if you want to wait with your submissions please do! Best regards Maja

Target Market(s)

Businesses and consumers

Industry/Entity Type

Health And Wellness

Number of Pages Required

5+ page

Font styles to use
Sans Serif

Colors
33a6d7
00a990
b7a5cd

Requirements
Must have
• Idea about pages:
• I am not sure how many pages I get for the price, but 5 would be nice to start with.
• Not sure what write ups is;-)
• But title of the pages could be:
• Landing page
• About us
• Services
• Retreats
• Contact us
Nice to have
• A clean and professional website but with some heart and soul in it. Because we Would love colours that harmonize with our logo, but other ideas are welcome!

```html
<!DOCTYPE html>
<html lang="en">
<head>
<meta charset="utf-8">
<title>Heartmeadow – Wellness</title>
<link href="https://fonts.googleapis.com/css2?family=Cinzel:wght@500;700&family=Open+Sans:wght@400&family=Poppins:wght@600&display=swap" rel="stylesheet">
<style>
:root{
  --navy:#0b2a5b;
  --teal:#1aa083;
  --aqua:#5fc9c4;
  --blue:#2a7fd0;
  --purple:#a990c6;
  --purple-deep:#9a7fbf;
  --sky-top:#8fc8ee;
  --sky-bottom:#ffffff;
  --text:#2b2b2b;
  --muted:#555;
  --white:#ffffff;
}
*{margin:0;padding:0;box-sizing:border-box}
html,body{width:1200px;height:2370px;overflow:hidden;background:var(--white)}
body{position:relative;font-family:"Open Sans",sans-serif;color:var(--text)}
.abs{position:absolute}
.btn{position:absolute;display:flex;align-items:center;justify-content:center;border-radius:30px;font-family:"Poppins",sans-serif;font-weight:600}

/* hero */
.hero{left:0;top:0;width:1200px;height:720px;background:linear-gradient(180deg,var(--sky-top) 0%,#cfe6f6 55%,var(--sky-bottom) 100%)}
.hero-photo{left:575px;top:100px;width:490px;height:500px;border-radius:50% 50% 40% 40%;background:radial-gradient(ellipse at 55% 45%,#b9c3d6 0%,#a5bfd8 45%,rgba(165,205,230,0) 72%)}
.logo{display:flex;align-items:center;gap:12px;font-family:"Cinzel",serif;font-weight:500;color:var(--navy);white-space:nowrap}
.logo-dot{border-radius:50%;border:3px solid var(--aqua);flex:none}
.nav{display:flex;justify-content:space-between;white-space:nowrap;font-family:"Cinzel",serif;font-weight:700;color:var(--navy)}
.nav .active{border-bottom:2px solid var(--aqua);padding-bottom:4px}
.main-nav{left:493px;top:50px;width:547px;font-size:16px}
.welcome{left:100px;top:236px;width:475px;text-align:center}
.welcome .pre{font-family:"Cinzel",serif;font-weight:700;font-size:32px;color:var(--aqua);line-height:40px}
.welcome h1{font-family:"Cinzel",serif;font-weight:700;font-size:50px;color:var(--navy);line-height:58px}
.welcome p{font-size:18px;line-height:25px;color:#222;margin-top:8px}
.arrow{width:44px;height:80px}

/* about */
.about-text{left:250px;top:752px;width:700px;text-align:center;color:var(--white)}
.about-text h2{font-family:"Cinzel",serif;font-weight:700;font-size:34px;line-height:44px;margin-bottom:14px}
.about-text p{font-size:17px;line-height:27px;margin-bottom:12px}

/* services */
.section-title{font-family:"Cinzel",serif;font-weight:700;font-size:31px;color:var(--navy);text-align:center}
.card{position:absolute;top:1271px;width:233px;height:339px;background:var(--white);border:1px solid #e2e2e2;box-shadow:0 1px 4px rgba(0,0,0,.08);text-align:center}
.card.featured{background:var(--teal);border-color:var(--teal)}
.card .icon{position:absolute;left:49px;top:38px;width:135px;height:98px}
.card h3{position:absolute;top:152px;width:100%;font-family:"Cinzel",serif;font-weight:700;font-size:22px;color:var(--teal)}
.card.featured h3,.card.featured p{color:var(--white)}
.card p{position:absolute;top:185px;left:12px;width:209px;font-size:13px;line-height:19.5px;color:var(--muted)}
.card .btn{left:43px;top:257px;width:146px;height:46px;border:2px solid var(--navy);color:var(--navy);font-size:15px}
.card.featured .btn{border-color:var(--white);color:var(--white)}
.dots{left:564px;top:1651px;display:flex;gap:8px}
.dots span{width:15px;height:15px;border-radius:50%;border:1.5px solid var(--teal)}
.dots .on{background:var(--teal)}

/* retreats */
.retreat-text{left:621px;top:1830px;width:450px;color:var(--white)}
.retreat-text h2{font-family:"Cinzel",serif;font-weight:700;font-size:34px;line-height:44px;margin-bottom:14px}
.retreat-text p{font-size:18.5px;line-height:26.5px;margin-bottom:13px;color:#f4ecfb}

/* footer */
.footer-nav{left:412px;top:2268px;width:494px;font-size:14px}
.copy{left:412px;top:2296px;font-size:14px;color:#333}
.social{display:flex;gap:6px}
.social span{width:33px;height:33px;border-radius:50%;background:var(--blue)}
</style>
</head>
<body>

<!-- Hero -->
<section class="abs hero">
  <div class="abs hero-photo" role="img" aria-label="Photo of a woman in a seated yoga stretch against a bright sky"></div>
</section>

<header>
  <div class="abs logo" style="left:168px;top:38px;font-size:24px;">
    <span class="logo-dot" style="width:58px;height:58px;"></span>
    <span>HEARTMEADOW</span>
  </div>
  <nav class="abs nav main-nav">
    <span class="active">HOME</span><span>ABOUT US</span><span>SERVICES</span><span>RETREATS</span><span>CONTACT US</span>
  </nav>
</header>

<div class="abs welcome">
  <div class="pre">WELCOME TO</div>
  <h1>HEARTMEADOW</h1>
  <p>Lorem ipsum dolor sit amet consectetuer<br>adipiscing elit Nam cursus Morbi</p>
</div>
<div class="btn" style="left:251px;top:412px;width:186px;height:57px;background:var(--navy);color:var(--white);font-size:19px;">Book Now</div>

<svg class="abs arrow" style="left:62px;top:308px" viewBox="0 0 44 80"><polyline points="36,4 4,40 36,76" fill="none" stroke="var(--navy)" stroke-width="3"/></svg>
<svg class="abs arrow" style="left:1102px;top:308px" viewBox="0 0 44 80"><polyline points="8,4 40,40 8,76" fill="none" stroke="var(--navy)" stroke-width="3"/></svg>

<!-- About band -->
<svg class="abs" style="left:0;top:630px" width="1200" height="505" viewBox="0 0 1200 505">
  <defs>
    <linearGradient id="aboutGrad" x1="0" y1="0" x2="1" y2="0">
      <stop offset="0" stop-color="#1f70c8"/>
      <stop offset="0.5" stop-color="#2a86c9"/>
      <stop offset="1" stop-color="#14a084"/>
    </linearGradient>
  </defs>
  <path d="M0 412 Q600 540 1200 402 L1200 420 Q600 555 0 430 Z" fill="var(--purple)"/>
  <path d="M0 77 Q600 -60 1200 77 L1200 402 Q600 540 0 412 Z" fill="url(#aboutGrad)" role="img" aria-label="Soft-focus photo of a relaxing massage treatment under a blue-green tint"/>
  <circle cx="600" cy="82" r="32" fill="none" stroke="var(--white)" stroke-width="4"/>
</svg>

<div class="abs about-text">
  <h2>ABOUT HEARTMEADOW</h2>
  <p>Pellentesque faucibus Ut accumsan ultricies elit Maecenas at justo id velit placerat molestie Donec dictum lectus non odio Cras a ante vitae enim</p>
  <p>Aaculis aliquam Mauris nunc quam venenatis nec euismod sit amet egestas placerat est Pellentesque habitant morbi tristique senectus et netus et malesuada fames ac turpis egestas Cras id elit Integer quis urna Ut ante enim</p>
</div>
<div class="btn" style="left:511px;top:987px;width:180px;height:56px;border:2px solid var(--white);color:var(--white);font-size:19px;">Read More</div>

<!-- Services -->
<h2 class="abs section-title" style="left:0;top:1198px;width:1177px;">OUR SERVICES</h2>

<div class="card featured" style="left:102px;">
  <svg class="icon" viewBox="0 0 135 98" role="img" aria-label="Yoga icon"><circle cx="67" cy="49" r="44" fill="none" stroke="#4fc1b2" stroke-width="5"/><circle cx="67" cy="49" r="20" fill="none" stroke="var(--white)" stroke-width="2.5"/></svg>
  <h3>YOGA</h3>
  <p>Lorem ipsum dolor sit amet consectetuer adipiscing elit Nam cursus Morbi ut mi Nullam</p>
  <div class="btn">Read More</div>
</div>
<div class="card" style="left:350px;">
  <svg class="icon" viewBox="0 0 135 98" role="img" aria-label="Massage stones icon"><circle cx="67" cy="49" r="44" fill="none" stroke="#a8e0dc" stroke-width="5"/><circle cx="67" cy="49" r="20" fill="none" stroke="var(--blue)" stroke-width="2.5"/></svg>
  <h3>MASSAGE</h3>
  <p>Lorem ipsum dolor sit amet consectetuer adipiscing elit Nam cursus Morbi ut mi Nullam</p>
  <div class="btn">Read More</div>
</div>
<div class="card" style="left:598px;">
  <svg class="icon" viewBox="0 0 135 98" role="img" aria-label="Healing sprout icon"><circle cx="67" cy="49" r="44" fill="none" stroke="#a8e0dc" stroke-width="5"/><circle cx="67" cy="49" r="20" fill="none" stroke="var(--blue)" stroke-width="2.5"/></svg>
  <h3>HEALING</h3>
  <p>Lorem ipsum dolor sit amet consectetuer adipiscing elit Nam cursus Morbi ut mi Nullam</p>
  <div class="btn">Read More</div>
</div>
<div class="card" style="left:846px;">
  <svg class="icon" viewBox="0 0 135 98" role="img" aria-label="Coaching mind icon"><circle cx="67" cy="49" r="44" fill="none" stroke="#a8e0dc" stroke-width="5"/><circle cx="67" cy="49" r="20" fill="none" stroke="var(--blue)" stroke-width="2.5"/></svg>
  <h3>COACHING</h3>
  <p>Lorem ipsum dolor sit amet consectetuer adipiscing elit Nam cursus Morbi ut mi Nullam</p>
  <div class="btn">Read More</div>
</div>

<div class="abs dots"><span></span><span class="on"></span><span></span></div>

<!-- Retreats -->
<svg class="abs" style="left:0;top:1650px" width="1200" height="572" viewBox="0 0 1200 572">
  <defs>
    <linearGradient id="retreatGrad" x1="0" y1="0" x2="1" y2="0">
      <stop offset="0" stop-color="#1d5f9c"/>
      <stop offset="0.3" stop-color="#3f7fb8"/>
      <stop offset="0.55" stop-color="#9b8fc6"/>
      <stop offset="1" stop-color="var(--purple)"/>
    </linearGradient>
  </defs>
  <path d="M0 5 Q600 140 1200 10 L1200 572 L0 572 Z" fill="url(#retreatGrad)" role="img" aria-label="Photo of a woman meditating on a wooden jetty by a lake, fading into lavender"/>
</svg>

<div class="abs retreat-text">
  <h2>RETREATS</h2>
  <p>Pellentesque faucibus Ut accumsan ultricies elit Maecenas at justo id velit placerat molestie</p>
  <p>Donec dictum lectus non odio Cras a ante vitae enim iaculis aliquam Mauris nunc quam venenatis nec euismod sit amet egestas placerat est</p>
</div>
<div class="btn" style="left:626px;top:2055px;width:162px;height:51px;border:2px solid var(--white);color:var(--white);font-size:17px;">Read More</div>

<!-- Footer -->
<footer>
  <div class="abs logo" style="left:152px;top:2257px;font-size:20px;">
    <span class="logo-dot" style="width:60px;height:60px;"></span>
    <span>HEARTMEADOW</span>
  </div>
  <nav class="abs nav footer-nav">
    <span>HOME</span><span>ABOUT US</span><span>SERVICES</span><span>RETREATS</span><span>CONTACT US</span>
  </nav>
  <div class="abs copy">© 2019 Company Name&nbsp; All right reserved</div>
  <div class="abs social" style="left:939px;top:2265px;" aria-label="Social links">
    <span style="background:#3a5ba8"></span><span style="background:#2a8fe0"></span><span style="background:#2a5f8a"></span>
  </div>
</footer>

</body>
</html>
```